Ecommerce Site for High End Watch repair

This high profile storefront is located in the heart of Manhattan and needs a complete new HIG H END look that will generate leads and sales for Vintage watches, straps and repairs of all kinds of watches.

The design should be based around the attached new logo, we will need to see the home page, a product results page with 4 watches at desktop view (1920x1080), a product detail view with the options to view multiple images, zoom in on images and have multiple upsell ability for straps, water proofing and customer reviews, plus a check out view. Flexible responsive Mobile/Tablet/Desktop design is imperative. Here are some competitors sites that the client likes
https://www.velmorastudio.example/
https://www.plinquaro.example/
https://www.drestwickandloom.example/
https://www.tuvenshoppe.example/
The Client is Ostrelle Hollow Watch, they do not have such a a large inventory as some of their competition but want to give the perception of top quality

We have a proprietary CMS in which we will implement your design so final product will need the fonts, graphics, color specifications and any other specialized css needed to produce the look.

Target Market(s)

high earners who like high end toys and fashionable clothes, watch collectors

Number of Pages Required

4 page

Requirements
Must have
• Home page that excites and at the same time shows intuitive navigation for the rest of the site
Product results page with high detail in each of 4 images
product detail page with multiple image view possibilities
Check out page with intuitive layout
Mobile view optimized
Highlight of repair services as well as sales
Nice to have
• customer reviews/testimonials
ways to display the watch detail innovatively
Place holders on the product detail page to upsell a wtch strap or add one of the services such as waterproofing or extended warranty

```html
<!DOCTYPE html>
<html lang="en">
<head>
<meta charset="utf-8">
<title>Ostrelle Hollow Watch — Home</title>
<link href="https://fonts.googleapis.com/css2?family=Cinzel:wght@400;600;700&family=Roboto:wght@400;500;700&display=swap" rel="stylesheet">
<style>
:root{
  --blue:#00a8ec;
  --blue-dark:#0a8fd0;
  --ink:#222;
  --text:#444;
  --muted:#888;
  --dark:#333333;
  --footer:#2f2f2f;
  --light:#f3f3f3;
  --hero-grey:#d5d7db;
  --line:#e4e4e4;
  --star:#f5c400;
  --white:#fff;
}
*{box-sizing:border-box;margin:0;padding:0}
html,body{width:1200px;height:4666px;overflow:hidden}
body{font-family:'Roboto',Arial,sans-serif;color:var(--text);background:var(--white);position:relative}
.page{position:relative;width:1200px;height:4666px}
.abs{position:absolute}
a{color:inherit;text-decoration:none}
.serif{font-family:'Cinzel',Georgia,serif}

/* header */
.header{left:0;top:0;width:1200px;height:114px;background:var(--white);z-index:3}
.topbar{position:absolute;top:32px;left:110px;font-size:11px;color:#333;display:flex;gap:34px;align-items:center}
.topbar span{display:flex;align-items:center;gap:7px}
.dot{width:10px;height:10px;border-radius:50%;background:#333;display:inline-block}
.nav{position:absolute;font-size:14px;color:#222;display:flex;gap:27px}
.nav-left{left:110px;top:79px}
.nav-right{left:770px;top:84px;gap:26px;align-items:center}
.account{position:absolute;right:200px;top:25px;display:flex;gap:10px}
.account a{font-size:10px;border:1px solid #999;padding:8px 14px;color:#333}
.icon-btns{position:absolute;left:1027px;top:26px;display:flex;gap:8px}
.icon-btns span{width:26px;height:26px;border-radius:50%;border:1px solid #999;display:flex;align-items:center;justify-content:center}
.icon-btns span.fill{background:#222;border-color:#222}
.logo-tab{left:493px;top:0;width:214px;height:141px;z-index:4}
.logo{position:absolute;left:0;right:0;top:24px;text-align:center;color:#444}
.logo-circle{width:46px;height:46px;border:2px solid #555;border-radius:50%;margin:0 auto 6px}
.logo-name{font-family:'Cinzel',Georgia,serif;font-size:13px;letter-spacing:1px;line-height:1.3;border-top:1px solid #777;border-bottom:1px solid #777;display:inline-block;padding:3px 6px}

/* hero */
.hero{left:0;top:114px;width:1200px;height:561px}
.hero-left{position:absolute;left:0;top:0;width:600px;height:100%;background:var(--blue)}
.hero-right{position:absolute;left:600px;top:0;width:600px;height:100%;background:var(--hero-grey)}
.hero-watch{position:absolute;left:485px;top:18px;width:235px;height:543px;border-radius:40px;background:linear-gradient(180deg,#3a2418 0%,#4a2d1d 22%,#c58a3e 34%,#a55a2a 48%,#c58a3e 60%,#3a2418 74%,#2e1c12 100%)}
.hero-copy{position:absolute;top:176px}
.hero-copy .kicker{font-size:15px;font-weight:500;margin-bottom:16px}
.hero-copy h1{font-family:'Cinzel',Georgia,serif;font-weight:400;font-size:37px;line-height:1.05;letter-spacing:1px}
.hero-left .hero-copy{left:110px;color:var(--white)}
.hero-right .hero-copy{left:163px;color:#222}
.hero-right h1{font-size:32px}
.btn-outline{display:inline-flex;align-items:center;gap:8px;margin-top:40px;height:51px;padding:0 22px;border:2px solid currentColor;font-size:15px;font-weight:700}
.slider-arrows{position:absolute;left:1000px;top:486px;display:flex;gap:15px}
.slider-arrows span{width:37px;height:37px;display:flex;align-items:center;justify-content:center}
.slider-arrows .on{background:var(--blue)}
.slider-arrows .off{background:#b0b3b8}

/* brands */
.brands{left:0;top:675px;width:1200px;height:229px;background:var(--dark);color:var(--white);text-align:center}
.section-title{font-family:'Cinzel',Georgia,serif;font-weight:600;letter-spacing:1px;color:#222}
.brands .section-title{color:var(--white);font-size:24px;margin-top:47px}
.brand-links{position:absolute;left:130px;top:89px;display:flex;gap:26px;font-size:14px}
.brand-links a{text-decoration:underline}
.brand-links .sep{margin-left:36px;margin-right:38px;text-decoration:none}
.brand-links .all{color:var(--blue)}
.search{position:absolute;left:410px;top:143px;display:flex}
.search .field{width:310px;height:34px;background:var(--white);color:#999;font-size:11px;padding:11px 10px;text-align:left}
.search .go{width:70px;height:34px;background:var(--blue);font-size:12px;font-weight:700;padding-top:10px}

/* products */
.picks{left:0;width:1200px;text-align:center}
.picks .section-title{font-size:33px;position:absolute;left:0;right:0}
.cards{position:absolute;left:105px;display:flex;gap:23px}
.card{width:230px;height:340px;border:1px solid var(--line);background:var(--white);text-align:center;padding-top:20px}
.card.active{border:2px solid #9ad8f2;background:#f7fcff}
.card .shot{width:150px;height:170px;margin:0 auto;border-radius:6px}
.card h3{font-size:16px;font-weight:500;color:#222;margin-top:20px}
.card p{font-size:12px;color:var(--muted);line-height:20px;margin:6px 20px 0}
.card .price{font-size:13px;color:#333;margin-top:10px}
.card .cart{font-size:14px;color:var(--blue);font-weight:500;margin-top:10px;display:flex;justify-content:center;align-items:center;gap:8px}
.side-arrow{position:absolute;top:0}
.btn-blue-outline{position:absolute;left:517px;width:166px;height:45px;border:2px solid var(--blue);color:var(--blue);font-size:14px;font-weight:500;display:flex;align-items:center;justify-content:center}

/* services */
.provide{left:0;top:1597px;width:1200px;height:445px;background:var(--light);text-align:center}
.provide .section-title{font-size:32px;margin-top:33px}
.services{position:absolute;left:180px;top:111px;display:flex;gap:30px}
.service{width:260px;height:240px;padding-top:36px}
.service.active{background:var(--white);box-shadow:0 2px 10px rgba(0,0,0,.08)}
.service h3{font-size:18px;font-weight:500;color:#222;margin-top:18px}
.service p{font-size:13px;color:var(--muted);line-height:22px;margin:12px 30px 0}

/* video */
.video{left:0;top:2042px;width:1200px;height:496px;background:radial-gradient(ellipse at 25% 45%,#7a6a45 0%,#3b3a36 35%,#1e1f22 75%)}
.play{position:absolute;left:563px;top:211px;width:74px;height:74px;border-radius:50%;background:var(--blue);display:flex;align-items:center;justify-content:center;border:4px solid rgba(255,255,255,.25)}

/* promo */
.promo-main{left:111px;top:3245px;width:462px;height:455px;background:linear-gradient(160deg,#3a3b3e,#232427);color:var(--white);text-align:center}
.promo-main h2{font-family:'Cinzel',Georgia,serif;font-weight:600;font-size:24px;line-height:35px;margin-top:187px;letter-spacing:.5px}
.promo-main .btn{display:inline-flex;margin-top:44px;height:45px;padding:0 24px;align-items:center;border:2px solid var(--blue);font-size:13px;font-weight:700}
.tile{width:236px;height:220px;background:#f2f2f2;text-align:center;font-size:13px;color:#222}
.tile .shot{width:120px;height:130px;margin:20px auto 0;border-radius:8px}
.tile .lbl{position:absolute;left:0;right:0;bottom:22px}
.tile .lbl.u{text-decoration:underline}

/* testimonials */
.clients{left:0;top:3820px;width:1200px;height:535px;background:#f7f7f7;text-align:center}
.clients .section-title{font-size:33px;margin-top:50px}
.quote{position:absolute;top:175px;width:310px;height:195px;background:var(--white);border-top:3px solid var(--blue);border-radius:6px;box-shadow:0 2px 8px rgba(0,0,0,.08)}
.quote p{font-size:13px;color:#555;line-height:25px;margin:72px 24px 0}
.avatar{position:absolute;left:50%;top:-48px;width:90px;height:90px;margin-left:-45px;border-radius:50%;border:3px solid var(--white);background:linear-gradient(160deg,#c7ccd3,#7c8590)}
.who{position:absolute;top:390px;width:310px;font-size:14px;color:#222;font-weight:500}
.who small{font-size:9px;font-weight:400}
.stars{display:flex;justify-content:center;gap:2px;margin-top:6px}

/* footer */
.footer{left:0;top:4355px;width:1200px;height:311px;background:var(--footer);color:var(--white)}
.f-logo{position:absolute;left:110px;top:56px;width:185px;text-align:center}
.f-logo .logo-circle{border-color:#ddd}
.f-logo .logo-name{border-color:#bbb;color:#ddd;font-size:14px}
.socials{display:flex;gap:6px;justify-content:center;margin-top:12px}
.socials span{width:24px;height:24px;border:1px solid #ccc;border-radius:50%}
.f-col{position:absolute;top:55px;font-size:11px;line-height:27px}
.f-col h4{font-size:12px;font-weight:700;margin-bottom:8px;letter-spacing:.3px}
.newsletter{position:absolute;left:703px;top:55px;font-size:11px}
.newsletter h4{font-size:12px;font-weight:700;margin-bottom:12px}
.newsletter p{line-height:18px;width:320px}
.nl-form{display:flex;gap:7px;margin-top:20px}
.nl-form .field{width:265px;height:43px;background:var(--white);color:#777;padding:15px 18px;font-size:11px}
.nl-form .go{width:113px;height:43px;background:var(--blue);font-size:14px;font-weight:700;display:flex;align-items:center;justify-content:center}
.copyright{position:absolute;left:0;right:0;top:272px;text-align:center;font-size:10px;color:#ddd}
.badge{position:absolute;left:118px;top:258px;width:42px;height:42px;border-radius:50%;background:#c9a227}
</style>
</head>
<body>
<div class="page">

<!-- header -->
<header class="abs header">
  <div class="topbar">
    <span><i class="dot"></i>JUNE 24, 10:45 AM</span>
    <span><svg width="10" height="10" viewBox="0 0 24 24"><path fill="#333" d="M6.6 10.8a15 15 0 006.6 6.6l2.2-2.2c.3-.3.7-.4 1-.2 1.1.4 2.3.6 3.6.6.6 0 1 .4 1 1V20c0 .6-.4 1-1 1A17 17 0 013 4c0-.6.4-1 1-1h3.5c.6 0 1 .4 1 1 0 1.2.2 2.4.6 3.6.1.3 0 .7-.2 1z"/></svg>(555) 014-2290</span>
  </div>
  <nav class="nav nav-left"><a>Home</a><a>About Us</a><a>Vintage Watches</a><a>Straps</a></nav>
  <div class="account"><a>LOG IN</a><a>SIGN UP</a></div>
  <div class="icon-btns">
    <span><svg width="12" height="11" viewBox="0 0 24 22"><path fill="none" stroke="#333" stroke-width="2" d="M12 20S2 13.5 2 7a5 5 0 0110-1 5 5 0 0110 1c0 6.5-10 13-10 13z"/></svg></span>
    <span class="fill"><svg width="13" height="12" viewBox="0 0 24 22"><path fill="#fff" d="M1 1h4l3 12h12l3-9H7"/><circle cx="10" cy="18" r="2" fill="#fff"/><circle cx="19" cy="18" r="2" fill="#fff"/></svg></span>
  </div>
  <nav class="nav nav-right"><a>Repairs</a><a>Shop</a><a>Press</a><a>Contact Us</a>
    <svg width="13" height="13" viewBox="0 0 24 24"><circle cx="10" cy="10" r="7" fill="none" stroke="#222" stroke-width="3"/><path d="M15 15l7 7" stroke="#222" stroke-width="3"/></svg></nav>
</header>

<div class="abs logo-tab">
  <svg width="214" height="141" style="position:absolute;left:0;top:0"><path d="M0 114 L0 0 L214 0 L214 114 L190 141 L24 141 Z" fill="#fff"/></svg>
  <div class="logo"><div class="logo-circle"></div><div class="logo-name">Ostrelle Hollow<br>Watch</div></div>
</div>

<!-- hero -->
<section class="abs hero">
  <div class="hero-left">
    <div class="hero-copy">
      <div class="kicker">Sales for Vintage Watches</div>
      <h1>AUTHENTICATED<br>LUXURY</h1>
      <a class="btn-outline">SHOP NOW <svg width="14" height="14" viewBox="0 0 24 24"><circle cx="12" cy="12" r="11" fill="#fff"/><path d="M10 7l5 5-5 5" stroke="#00a8ec" stroke-width="3" fill="none"/></svg></a>
    </div>
  </div>
  <div class="hero-right">
    <div class="hero-copy">
      <div class="kicker">Expert Watch Repair NYC</div>
      <h1>Professional,<br>Swiss Watch Repair</h1>
      <a class="btn-outline">LEARN MORE <svg width="14" height="14" viewBox="0 0 24 24"><circle cx="12" cy="12" r="11" fill="#222"/><path d="M10 7l5 5-5 5" stroke="#d5d7db" stroke-width="3" fill="none"/></svg></a>
    </div>
  </div>
  <div class="hero-watch" role="img" aria-label="Vintage gold wristwatch with wood-grain dial on a brown leather strap"></div>
  <div class="slider-arrows">
    <span class="on"><svg width="12" height="14" viewBox="0 0 12 14"><path d="M8 2L3 7l5 5" stroke="#fff" stroke-width="2" fill="none"/></svg></span>
    <span class="off"><svg width="12" height="14" viewBox="0 0 12 14"><path d="M4 2l5 5-5 5" stroke="#fff" stroke-width="2" fill="none"/></svg></span>
  </div>
</section>

<!-- brands -->
<section class="abs brands">
  <h2 class="section-title">SHOP POPULAR BRANDS</h2>
  <div class="brand-links">
    <a>Valdrenne</a><a>CORVANE</a><a>Halbrook</a><a>Strevik</a><a>Musselle</a><a>Oberlin Kade</a><a>Ravel</a><a>Lissandre</a><a>Amsel Vauquier</a>
    <span class="sep">|</span><a class="all">VIEW ALL BRANDS</a>
  </div>
  <div class="search"><div class="field">SEARCH 2,500+ WATCHES</div><div class="go">SEARCH</div></div>
</section>

<!-- top watch picks -->
<section class="abs picks" style="top:904px;height:693px">
  <h2 class="section-title" style="top:71px">TOP WATCH PICKS</h2>
  <svg class="side-arrow" style="left:38px;top:300px" width="20" height="40" viewBox="0 0 20 40"><path d="M16 4L4 20l12 16" stroke="#bbb" stroke-width="3" fill="none"/></svg>
  <svg class="side-arrow" style="left:1142px;top:300px" width="20" height="40" viewBox="0 0 20 40"><path d="M4 4l12 16L4 36" stroke="#bbb" stroke-width="3" fill="none"/></svg>
  <div class="cards" style="top:151px">
    <div class="card"><div class="shot" role="img" aria-label="Steel watch with grey dial on bracelet" style="background:linear-gradient(180deg,#c9cbcd,#56595d,#c9cbcd)"></div><h3>Tessoro 4072</h3><p>Sed ut perspiciatis unde omnis sit voluptatem</p><div class="price">$24,321</div><div class="cart">Add to Cart <span style="color:#bbb">|</span><svg width="13" height="12" viewBox="0 0 24 22"><path fill="none" stroke="#00a8ec" stroke-width="2" d="M12 20S2 13.5 2 7a5 5 0 0110-1 5 5 0 0110 1c0 6.5-10 13-10 13z"/></svg></div></div>
    <div class="card active"><div class="shot" role="img" aria-label="Silver chronograph watch with white dial on brown strap" style="background:linear-gradient(180deg,#6b4a35,#e9e7e2,#6b4a35)"></div><h3>Tessoro 4072</h3><p>Sed ut perspiciatis unde omnis sit voluptatem</p><div class="price">$24,321</div><div class="cart">Add to Cart <span style="color:#bbb">|</span><svg width="13" height="12" viewBox="0 0 24 22"><path fill="none" stroke="#00a8ec" stroke-width="2" d="M12 20S2 13.5 2 7a5 5 0 0110-1 5 5 0 0110 1c0 6.5-10 13-10 13z"/></svg></div></div>
    <div class="card"><div class="shot" role="img" aria-label="Gold watch with wood dial on dark leather strap" style="background:linear-gradient(180deg,#3a2418,#b5783a,#3a2418)"></div><h3>Tessoro 4072</h3><p>Sed ut perspiciatis unde omnis sit voluptatem</p><div class="price">$24,321</div><div class="cart">Add to Cart <span style="color:#bbb">|</span><svg width="13" height="12" viewBox="0 0 24 22"><path fill="none" stroke="#00a8ec" stroke-width="2" d="M12 20S2 13.5 2 7a5 5 0 0110-1 5 5 0 0110 1c0 6.5-10 13-10 13z"/></svg></div></div>
    <div class="card"><div class="shot" role="img" aria-label="Gold chronograph with cream dial on brown strap" style="background:linear-gradient(180deg,#7a4a2a,#e8dcc0,#7a4a2a)"></div><h3>Tessoro 4072</h3><p>Sed ut perspiciatis unde omnis sit voluptatem</p><div class="price">$24,321</div><div class="cart">Add to Cart <span style="color:#bbb">|</span><svg width="13" height="12" viewBox="0 0 24 22"><path fill="none" stroke="#00a8ec" stroke-width="2" d="M12 20S2 13.5 2 7a5 5 0 0110-1 5 5 0 0110 1c0 6.5-10 13-10 13z"/></svg></div></div>
  </div>
  <a class="btn-blue-outline" style="top:551px">SHOP WATCHES</a>
</section>

<!-- we provide -->
<section class="abs provide">
  <h2 class="section-title">We provide</h2>
  <div class="services">
    <div class="service">
      <svg width="46" height="64" viewBox="0 0 46 64"><rect x="13" y="2" width="20" height="12" rx="2" fill="none" stroke="#00a8ec" stroke-width="2.5"/><rect x="13" y="50" width="20" height="12" rx="2" fill="none" stroke="#00a8ec" stroke-width="2.5"/><circle cx="23" cy="32" r="18" fill="none" stroke="#00a8ec" stroke-width="2.5"/><path d="M23 22v10h8" stroke="#00a8ec" stroke-width="2.5" fill="none"/></svg>
      <h3>Vintage Watches</h3><p>Sed ut perspiciatis unde omnis iste natus error sit voluptatem</p>
    </div>
    <div class="service active">
      <svg width="84" height="72" viewBox="0 0 84 72"><circle cx="42" cy="36" r="36" fill="#eef0f2"/><circle cx="38" cy="38" r="14" fill="none" stroke="#00a8ec" stroke-width="2.5"/><rect x="31" y="14" width="14" height="9" fill="none" stroke="#00a8ec" stroke-width="2.5"/><rect x="31" y="53" width="14" height="9" fill="none" stroke="#00a8ec" stroke-width="2.5"/><path d="M38 31v7h6M54 26l8 26" stroke="#00a8ec" stroke-width="2.5" fill="none"/></svg>
      <h3>Watch Repair</h3><p>Sed ut perspiciatis unde omnis iste natus error sit voluptatem</p>
    </div>
    <div class="service">
      <svg width="56" height="60" viewBox="0 0 56 60"><rect x="6" y="2" width="16" height="56" rx="3" fill="none" stroke="#00a8ec" stroke-width="2.5"/><rect x="34" y="2" width="16" height="56" rx="3" fill="none" stroke="#00a8ec" stroke-width="2.5"/><path d="M6 14h16M34 14h16M14 28v10M42 36v8" stroke="#00a8ec" stroke-width="2.5"/></svg>
      <h3>Straps</h3><p>Sed ut perspiciatis unde omnis iste natus error sit voluptatem</p>
    </div>
  </div>
</section>

<!-- video -->
<section class="abs video" role="img" aria-label="Close-up of a watchmaker's hands servicing a gold movement with tweezers">
  <div class="play"><svg width="26" height="28" viewBox="0 0 26 28"><path d="M4 2l20 12L4 26z" fill="#fff"/></svg></div>
</section>

<!-- top straps picks -->
<section class="abs picks" style="top:2538px;height:707px">
  <h2 class="section-title" style="top:84px">TOP STRAPS PICKS</h2>
  <svg class="side-arrow" style="left:38px;top:313px" width="20" height="40" viewBox="0 0 20 40"><path d="M16 4L4 20l12 16" stroke="#bbb" stroke-width="3" fill="none"/></svg>
  <svg class="side-arrow" style="left:1142px;top:313px" width="20" height="40" viewBox="0 0 20 40"><path d="M4 4l12 16L4 36" stroke="#bbb" stroke-width="3" fill="none"/></svg>
  <div class="cards" style="top:164px">
    <div class="card"><div class="shot" role="img" aria-label="Pair of dark brown leather straps" style="width:80px;background:linear-gradient(90deg,#3a1c14 0 40%,transparent 40% 60%,#3a1c14 60%)"></div><h3>Straps Title</h3><p>Sed ut perspiciatis unde omnis sit voluptatem</p><div class="price">$24,321</div><div class="cart">Add to Cart <span style="color:#bbb">|</span><svg width="13" height="12" viewBox="0 0 24 22"><path fill="none" stroke="#00a8ec" stroke-width="2" d="M12 20S2 13.5 2 7a5 5 0 0110-1 5 5 0 0110 1c0 6.5-10 13-10 13z"/></svg></div></div>
    <div class="card active"><div class="shot" role="img" aria-label="Pair of navy blue leather straps" style="width:80px;background:linear-gradient(90deg,#1d2a6b 0 40%,transparent 40% 60%,#1d2a6b 60%)"></div><h3>Straps Title</h3><p>Sed ut perspiciatis unde omnis sit voluptatem</p><div class="price">$24,321</div><div class="cart">Add to Cart <span style="color:#bbb">|</span><svg width="13" height="12" viewBox="0 0 24 22"><path fill="none" stroke="#00a8ec" stroke-width="2" d="M12 20S2 13.5 2 7a5 5 0 0110-1 5 5 0 0110 1c0 6.5-10 13-10 13z"/></svg></div></div>
    <div class="card"><div class="shot" role="img" aria-label="Gold, steel and rose-gold metal bracelets" style="width:130px;background:linear-gradient(90deg,#d8b13e 0 22%,transparent 22% 39%,#b9bcb6 39% 61%,transparent 61% 78%,#e09a4a 78%)"></div><h3>Straps Title</h3><p>Sed ut perspiciatis unde omnis sit voluptatem</p><div class="price">$24,321</div><div class="cart">Add to Cart <span style="color:#bbb">|</span><svg width="13" height="12" viewBox="0 0 24 22"><path fill="none" stroke="#00a8ec" stroke-width="2" d="M12 20S2 13.5 2 7a5 5 0 0110-1 5 5 0 0110 1c0 6.5-10 13-10 13z"/></svg></div></div>
    <div class="card"><div class="shot" role="img" aria-label="Pair of burgundy leather straps" style="width:80px;background:linear-gradient(90deg,#4a1626 0 40%,transparent 40% 60%,#4a1626 60%)"></div><h3>Straps Title</h3><p>Sed ut perspiciatis unde omnis sit voluptatem</p><div class="price">$24,321</div><div class="cart">Add to Cart <span style="color:#bbb">|</span><svg width="13" height="12" viewBox="0 0 24 22"><path fill="none" stroke="#00a8ec" stroke-width="2" d="M12 20S2 13.5 2 7a5 5 0 0110-1 5 5 0 0110 1c0 6.5-10 13-10 13z"/></svg></div></div>
  </div>
  <a class="btn-blue-outline" style="top:562px">SHOP WATCHES</a>
</section>

<!-- promo grid -->
<section class="abs promo-main" role="img" aria-label="Dimmed photo of a watch movement behind the headline">
  <h2>SHOP CERTIFIED PRE-OWNED<br>WATCHES &amp; STRAPS</h2>
  <a class="btn">SHOP CERTIFIED PRE-OWNED</a>
</section>
<div class="abs tile" style="left:600px;top:3245px"><div class="shot" role="img" aria-label="Rose gold diver watch with black dial" style="width:70px;background:linear-gradient(180deg,#d8a58a,#1e1e1e,#d8a58a)"></div><div class="lbl u">VALDRENNE WATCHES</div></div>
<div class="abs tile" style="left:852px;top:3245px"><div class="shot" role="img" aria-label="Brown leather strap with gold buckle" style="width:180px;height:40px;margin-top:58px;background:#5a2a1c"></div><div class="lbl u">BRANDED STRAPS</div></div>
<div class="abs tile" style="left:600px;top:3483px"><div class="shot" role="img" aria-label="Two-tone chronograph with black dial on gold bracelet" style="width:110px;background:radial-gradient(circle,#1b2230 0 45%,#c9a640 46% 60%,#eee 61%)"></div><div class="lbl">WATCHES UNDER $2,000</div></div>
<div class="abs tile" style="left:852px;top:3483px"><div class="shot" role="img" aria-label="Tan leather strap with silver buckle" style="width:190px;height:40px;margin-top:58px;background:#a1461f;transform:rotate(-14deg)"></div><div class="lbl">STRAPS UNDER $2,000</div></div>

<!-- testimonials -->
<section class="abs clients">
  <h2 class="section-title">What Our Clients Say</h2>
  <div class="quote" style="left:111px"><div class="avatar" role="img" aria-label="Client portrait"></div><p>Sed ut perspiciatis unde omnis iste natus error sit voluptatem accusantium doloremque laudantium, totam rem aperiam, eaque ipsa</p></div>
  <div class="quote" style="left:445px"><div class="avatar" role="img" aria-label="Client portrait"></div><p>Sed ut perspiciatis unde omnis iste natus error sit voluptatem accusantium doloremque laudantium, totam rem aperiam, eaque ipsa</p></div>
  <div class="quote" style="left:779px"><div class="avatar" role="img" aria-label="Client portrait"></div><p>Sed ut perspiciatis unde omnis iste natus error sit voluptatem accusantium doloremque laudantium, totam rem aperiam, eaque ipsa</p></div>
  <div class="who" style="left:111px">Delia Marrow, <small>Chairman WBI</small><div class="stars"><svg width="70" height="12" viewBox="0 0 70 12"><g fill="#f5c400"><path id="st" d="M6 0l1.8 4 4.2.4-3.2 2.8 1 4.2L6 9.2 2.2 11.4l1-4.2L0 4.4 4.2 4z"/><use href="#st" x="14"/><use href="#st" x="28"/><use href="#st" x="42"/><use href="#st" x="56"/></g></svg></div></div>
  <div class="who" style="left:445px">Inez Calloway, <small>Project Manager</small><div class="stars"><svg width="70" height="12" viewBox="0 0 70 12"><g fill="#f5c400"><use href="#st"/><use href="#st" x="14"/><use href="#st" x="28"/><use href="#st" x="42"/><use href="#st" x="56"/></g></svg></div></div>
  <div class="who" style="left:779px">Tobin Hartwell, <small>Chairman WBI</small><div class="stars"><svg width="70" height="12" viewBox="0 0 70 12"><g fill="#f5c400"><use href="#st"/><use href="#st" x="14"/><use href="#st" x="28"/><use href="#st" x="42"/><use href="#st" x="56"/></g></svg></div></div>
</section>

<!-- footer -->
<footer class="abs footer">
  <div class="f-logo"><div class="logo-circle"></div><div class="logo-name">Ostrelle Hollow Watch</div>
    <div class="socials"><span></span><span></span><span></span><span></span></div></div>
  <div class="f-col" style="left:362px"><h4>COMPANY</h4><div>Home</div><div>About Us</div><div>Vintage watches</div><div>Straps</div><div>Repairs</div></div>
  <div class="f-col" style="left:517px"><h4>INFORMATION</h4><div>Terms &amp; Conditions</div><div>Privacy Policy</div><div>Disclaimer</div><div>Site Map</div><div>Categories</div></div>
  <div class="newsletter"><h4>SUBSCRIBE OUR NEWSLETTER</h4><p>Subscribe to our mailing list to receives daily updates direct to your inbox!</p>
    <div class="nl-form"><div class="field">Email Address</div><div class="go">SUBSCRIBE</div></div></div>
  <div class="badge"></div>
  <div class="copyright">Copyrights © Ostrelle Hollow Watch | Allrights Reserved</div>
</footer>

</div>
</body>
</html>
```